business card for author of crime novel

I am an author with a new book. I need a business card with the book's cover on one side (already uploaded), and contact details on the other.

Walt Pemberty
Author

telephone: 646-512-7380
website: www.waltpemberty.net
facebook: pagefolk.com/wpemberty
twitter: chatterbox.net/wpemberty
email: wpemberty@postvale.net

Target Market(s)

Readers of mystery books

Industry/Entity Type

Business

Contact Information for Business Card

Walt Pemberty
Author

telephone: 646-512-7380

Font styles to use
Serif
Sans Serif

Requirements
Must have
• Book cover on one side. My contact info on the other, with the name of the book repeated if that makes sense. Clean design.
Should not have
• Overly ornate, too formal, too distracting

```html
<!DOCTYPE html>
<html lang="en">
<head>
<meta charset="utf-8">
<title>Walt Pemberty – Author Business Card</title>
<link rel="stylesheet" href="https://fonts.googleapis.com/css2?family=Rye&family=Cinzel:wght@400&family=IM+Fell+English&family=Noto+Sans:wght@400&display=swap">
<style>
  :root {
    --backdrop: #afa37e;
    --cover-gold: #c98b0a;
    --ink: #1c1a12;
    --paper: #ffffff;
    --photo-dark: #2f5559;
    --photo-mid: #4f8a8c;
    --photo-light: #a9c7c4;
    --name-yellow: #f4e320;
    --scrap: #e9d6a0;
    --scrap-edge: #c9b27a;
    --card-shadow: 4px 5px 6px rgba(40, 34, 20, 0.45);
  }
  * { box-sizing: border-box; margin: 0; padding: 0; }
  html, body { width: 1200px; height: 840px; overflow: hidden; }
  body { background: var(--backdrop); position: relative; }

  .card {
    position: absolute;
    top: 75px;
    width: 412px;
    height: 684px;
    box-shadow: var(--card-shadow);
  }

  /* Front: book cover */
  .card--cover { left: 140px; background: var(--cover-gold); }
  .cover__title {
    position: absolute; top: 68px; left: 0; width: 100%;
    text-align: center;
    font-family: "Rye", serif;
    font-weight: 400;
    font-size: 28px; letter-spacing: 1px;
    color: var(--ink);
  }
  .cover__photo {
    position: absolute; left: 50px; top: 127px;
    width: 313px; height: 417px;
    background:
      radial-gradient(ellipse at 20% 10%, var(--photo-light) 0%, transparent 45%),
      linear-gradient(160deg, var(--photo-mid) 0%, var(--photo-dark) 75%, #203c40 100%);
  }
  .cover__author {
    position: absolute; right: 8px; bottom: 10px; width: 172px;
    text-align: center;
    font-family: "Cinzel", serif;
    font-size: 22px; line-height: 1.1;
    color: var(--name-yellow);
  }
  .cover__series {
    position: absolute; left: 48px; top: 561px;
    width: 317px; height: 55px;
    background: var(--scrap);
    border: 1px solid var(--scrap-edge);
    border-radius: 4px;
    box-shadow: 2px 3px 3px rgba(60, 40, 0, 0.35);
    display: flex; align-items: center; justify-content: center;
    font-family: "IM Fell English", serif;
    font-size: 25px; color: var(--ink);
  }

  /* Back: contact details */
  .card--contact { left: 656px; background: var(--paper); }
  .contact__name {
    position: absolute; top: 74px; left: 0; width: 100%;
    text-align: center;
    font-family: "Noto Sans", sans-serif;
    font-weight: 400;
    font-size: 40px; color: var(--ink);
  }
  .contact__role {
    position: absolute; top: 129px; left: 0; width: 100%; height: 40px;
    background: var(--ink);
    color: var(--paper);
    font-family: "Noto Sans", sans-serif;
    font-size: 25px; line-height: 40px; text-align: center;
  }
  .contact__list {
    position: absolute; left: 69px; top: 464px;
    list-style: none;
    font-family: "Noto Sans", sans-serif;
    font-size: 16.5px; color: var(--ink);
  }
  .contact__item { display: flex; align-items: center; height: 25.5px; }
  .contact__icon {
    width: 18px; height: 18px; margin-right: 25px;
    display: flex; align-items: center; justify-content: center;
    font-size: 16px;
  }
  .contact__square { width: 16px; height: 16px; background: var(--ink); border-radius: 2px; }
</style>
</head>
<body>
  <section class="card card--cover">
    <h1 class="cover__title">DEAD AIR AVENUE</h1>
    <div class="cover__photo" role="img" aria-label="Teal-toned photograph of a tall brick tenement building with fire escapes">
      <p class="cover__author">WALT<br>PEMBERTY</p>
    </div>
    <p class="cover__series">A Desmond Hale Mystery</p>
  </section>

  <section class="card card--contact">
    <h2 class="contact__name">Walt Pemberty</h2>
    <p class="contact__role">Author</p>
    <ul class="contact__list">
      <li class="contact__item">
        <span class="contact__icon">
          <svg width="17" height="14" viewBox="0 0 17 14" aria-hidden="true">
            <path d="M1 5 Q8.5 -1 16 5 L13 6 L12 4 Q8.5 3 5 4 L4 6 Z" fill="#1c1a12"/>
            <path d="M4 7 L13 7 L15 13 L2 13 Z" fill="#1c1a12"/>
            <circle cx="8.5" cy="10" r="1.6" fill="#fff"/>
          </svg>
        </span>646-512-7380
      </li>
      <li class="contact__item">
        <span class="contact__icon">
          <svg width="16" height="16" viewBox="0 0 16 16" aria-hidden="true">
            <circle cx="8" cy="8" r="7" fill="none" stroke="#1c1a12" stroke-width="1.5"/>
            <ellipse cx="8" cy="8" rx="3" ry="7" fill="none" stroke="#1c1a12" stroke-width="1.2"/>
            <line x1="1" y1="8" x2="15" y2="8" stroke="#1c1a12" stroke-width="1.2"/>
          </svg>
        </span>www.waltpemberty.net
      </li>
      <li class="contact__item"><span class="contact__icon"><span class="contact__square"></span></span>pagefolk.com/wpemberty</li>
      <li class="contact__item"><span class="contact__icon"><span class="contact__square"></span></span>chatterbox.net/wpemberty</li>
      <li class="contact__item"><span class="contact__icon">@</span>wpemberty@postvale.net</li>
    </ul>
  </section>
</body>
</html>
```